Quellmarrow Website & website development in Wordpress

Simple website for a 5 pages with some 15 products for sale.
We will sell T shirts and other Viking mens grooming products.

*****Lady barbers****
Also the company that gets awarded this job needs to be able to give me a quote to build the site in wordpress, just a design will not work.

Target Market(s)

The adventurous person likes to travels and get a good haircut

Coding

Coded - Design and coding required

Number of Pages Required

5+ page

Font styles to use
Sans Serif

Colors
3176b5
33a6d7

Requirements
Must have
• Must have a product order page for T-Shirts
Must have a travel adventure page with up to 5 recommended adventures
Must have a link to our instagram @quellmarrowparlor page that would allow a client to book a haircut
Should show female stylists cutting mens hair- So far the only pictures in the designs submitted are male barbers
Nice to have
• We have this set up in NetOrca would like to use wordpress. Thanks!

```html
<!DOCTYPE html>
<html lang="en">
<head>
<meta charset="utf-8">
<title>Quellmarrow – Home</title>
<link href="https://fonts.googleapis.com/css2?family=Playfair+Display:wght@900&family=Roboto:wght@400;500;700&display=swap" rel="stylesheet">
<style>
:root{
  --red:#c8102e;
  --navy:#1f3f8f;
  --cream:#f8f2e8;
  --ink:#1c1c1c;
  --grey:#7a7a7a;
  --footer:#2c2c2c;
  --line:#dcd5ca;
}
*{box-sizing:border-box;margin:0;padding:0}
html,body{width:1200px;height:4286px;overflow:hidden}
body{position:relative;background:var(--cream);font-family:'Roboto',sans-serif;color:var(--ink)}
.abs{position:absolute}
.serif{font-family:'Playfair Display',serif;font-weight:900;letter-spacing:1.5px}

/* top bar */
.topbar{left:0;top:0;width:1200px;height:38px;background:var(--red);color:#fff;font-size:13px;font-weight:700}
.topbar .tag{left:110px;top:11px}
.topbar .links{left:717px;top:11px;display:flex;gap:32px}
.topbar .social{left:992px;top:12px;display:flex;gap:10px}
.dot{width:13px;height:13px;border-radius:50%;background:#fff}

/* header */
.logo{left:105px;top:48px;width:92px;height:118px;display:flex;flex-direction:column;align-items:center;justify-content:center;gap:8px}
.logo .mark{width:34px;height:34px;border-radius:50%;background:var(--red)}
.logo span{font-size:15px;font-weight:700;color:var(--navy)}
.search{left:360px;top:70px;width:374px;height:40px;border:1px solid #cfc8bc;border-radius:20px;background:#fff;font-size:14px;color:#888;padding:11px 22px}
.search .btn{position:absolute;right:3px;top:3px;width:32px;height:32px;border-radius:50%;background:var(--navy)}
.account{left:832px;top:81px;font-size:14px;color:#444;display:flex;gap:28px}
.nav{left:256px;top:137px;display:flex;font-size:14px;font-weight:700}
.nav a{color:var(--ink);text-decoration:none;margin-right:47px;padding-bottom:8px}
.nav a.active{color:var(--red);border-bottom:2px solid var(--red)}

/* hero */
.hero{left:0;top:178px;width:1200px;height:558px;background:linear-gradient(100deg,#3b2a22 0%,#7a5038 38%,#c08a5a 55%,#3b2a28 100%)}
.hero h1{position:absolute;left:110px;top:145px;color:#fff;font-size:52px;line-height:58px}
.hero p{position:absolute;left:111px;top:285px;width:560px;color:#f3e6da;font-size:14px;line-height:22px}
.pill{display:inline-flex;align-items:center;gap:8px;background:var(--red);color:#fff;font-weight:700;font-size:13px;border-radius:26px}
.hero .pill{position:absolute;left:111px;top:359px;height:51px;padding:0 42px 0 30px}
.dots{position:absolute;left:574px;top:484px;display:flex;gap:3px}
.dots i{width:8px;height:8px;border-radius:50%;background:#fff}
.dots i.off{background:#cfc4b8}

/* categories */
.cat{top:824px;width:483px;height:388px;display:flex;align-items:flex-end;justify-content:center;padding-bottom:34px;color:#fff;font-weight:700;font-size:18px}
.cat.shirts{left:110px;background:linear-gradient(135deg,#e79a8f,#c94f4f 60%,#d44a4a)}
.cat.grooming{left:607px;background:linear-gradient(160deg,#c7c0cf,#7c7da6 50%,#2f4a8e)}

/* section heads */
.sec-head{left:110px;width:980px;border-bottom:2px solid var(--line);padding-bottom:8px;display:flex;justify-content:space-between;align-items:flex-end}
.sec-head h2{font-size:28px}
.sec-head h2::after{content:"";position:absolute;left:0;bottom:-10px;width:55px;height:2px;background:#999}
.sec-head a{font-size:12px;font-weight:700;color:var(--red);text-decoration:underline;margin-bottom:4px}

/* product cards */
.row{left:110px;display:flex;gap:9px}
.card{position:relative;width:238px;height:314px;background:#fff;box-shadow:0 1px 4px rgba(0,0,0,.08);padding:0 34px}
.card.faded{opacity:.45;background:transparent;box-shadow:none}
.card .img{width:120px;height:130px;margin:20px auto 0;border-radius:4px}
.card h3{font-size:13px;font-weight:700;margin-top:27px}
.card .sub{font-size:13px;color:var(--grey);margin-top:13px}
.card .price{font-size:21px;font-weight:500;color:var(--red);margin-top:18px}
.card .old{font-size:12px;color:#aaa;text-decoration:line-through;margin-top:4px;font-weight:700}
.card .cart{position:absolute;right:32px;bottom:24px;width:38px;height:38px;border-radius:50%;background:var(--navy)}
.card .cart::after{content:"";position:absolute;left:12px;top:13px;width:14px;height:10px;border:2px solid #fff;border-top-width:3px;border-radius:0 0 2px 2px}
.badge{position:absolute;background:var(--red);color:#fff;font-size:9px;font-weight:700;padding:2px 8px}
.stock{position:absolute;left:13px;top:142px;background:#888;color:#222;font-size:11px;padding:5px 10px}
.tools{position:absolute;right:14px;top:12px;width:30px;height:90px;background:#fff;box-shadow:0 0 3px rgba(0,0,0,.15);display:flex;flex-direction:column;align-items:center;justify-content:space-around}
.tools i{width:10px;height:10px;border:2px solid #222;border-radius:50%}

/* banner */
.banner{left:0;top:1830px;width:1200px;height:386px;background:linear-gradient(100deg,#223247 0%,#6f89a3 40%,#b7a08e 70%,#8b5a44 100%)}
.banner .kick{position:absolute;left:111px;top:70px;color:#fff;font-size:13px;font-weight:700}
.banner h2{position:absolute;left:110px;top:102px;color:#fff;font-size:38px;line-height:44px}
.banner p{position:absolute;left:111px;top:210px;color:#e7ebf0;font-size:15px}
.banner .pill{position:absolute;left:111px;top:265px;height:48px;padding:0 28px 0 18px}

/* testimonials */
.quote{top:2927px;width:475px;height:235px;background:#fff;box-shadow:0 1px 4px rgba(0,0,0,.08)}
.quote .photo{position:absolute;left:36px;top:46px;width:115px;height:145px;border:3px solid #eee;background:linear-gradient(180deg,#d9dee4,#6f87aa)}
.quote .stars{position:absolute;left:190px;top:44px;color:#f08a1c;font-size:20px;letter-spacing:3px}
.quote .mark{position:absolute;right:27px;top:24px;font-family:'Playfair Display',serif;font-size:80px;line-height:80px;color:var(--red)}
.quote p{position:absolute;left:190px;top:85px;width:240px;font-size:14px;line-height:26px;color:#666;text-align:justify}
.quote .who{position:absolute;right:46px;top:195px;font-size:13px;font-weight:700;color:var(--navy)}

/* about */
.about-img{left:111px;top:3290px;width:440px;height:377px;border:4px solid #fff;background:linear-gradient(180deg,#2d3440,#6a6466 50%,#8c857c)}
.about h2{position:absolute;left:622px;top:3295px;font-size:32px}
.about p{position:absolute;left:622px;top:3358px;width:458px;font-size:13.5px;line-height:29.5px;color:#555;text-align:justify}
.about .pill{position:absolute;left:622px;top:3614px;height:45px;padding:0 24px}

/* footer */
.footer{left:0;top:3777px;width:1200px;height:509px;background:var(--footer);color:#fff}
.news{position:absolute;left:178px;top:72px;font-size:21px;font-weight:700}
.email{position:absolute;left:478px;top:58px;width:402px;height:50px;background:#fff;color:#666;font-size:14px;padding:17px 24px 0 58px}
.email::before{content:"";position:absolute;left:24px;top:19px;width:16px;height:11px;border:2px solid var(--red)}
.subscribe{position:absolute;left:880px;top:58px;width:142px;height:50px;background:var(--red);border:2px solid #fff;font-weight:700;font-size:16px;display:flex;align-items:center;justify-content:center}
.rule{position:absolute;left:111px;width:976px;height:1px;background:#555}
.flogo{position:absolute;left:111px;top:215px;width:100px;height:95px;display:flex;flex-direction:column;align-items:center;gap:8px}
.flogo .mark{width:32px;height:32px;border-radius:50%;background:var(--red)}
.flogo span{font-weight:700;font-size:15px}
.fsocial{position:absolute;left:112px;top:375px;display:flex;gap:8px}
.fsocial i{width:33px;height:33px;border:2px solid #fff;border-radius:50%}
.col h4{font-size:13px;font-weight:700;text-decoration:underline;margin-bottom:14px}
.col{position:absolute;top:222px;font-size:13px}
.col li{list-style:none;margin-bottom:16px}
.col li::before{content:"»";margin-right:12px}
.ci{display:flex;align-items:flex-start;gap:22px;margin-bottom:30px;line-height:20px}
.ci .ic{flex:none;width:30px;height:30px;border:2px solid #fff;border-radius:50%}
.copy{position:absolute;left:113px;top:470px;font-size:13px}
.cards{position:absolute;left:958px;top:467px;display:flex;gap:4px}
.cards i{width:22px;height:16px;background:#e6e6e6;border-radius:2px}
</style>
</head>
<body>

<header>
  <div class="abs topbar">
    <div class="abs tag">BUILD A BETTER BRAND TODAY!</div>
    <div class="abs links"><span>ABOUT</span><span>NEWS</span><span>CONTACT</span></div>
    <div class="abs social"><i class="dot"></i><i class="dot"></i><i class="dot"></i><i class="dot"></i></div>
  </div>
  <div class="abs logo"><i class="mark"></i><span>Quellmarrow</span></div>
  <div class="abs search">Search<span class="btn"></span></div>
  <div class="abs account"><span>◯ Log in / Register</span><span>🛒 (0) Items</span></div>
  <nav class="abs nav">
    <a class="active">HOME</a><a>WHAT WE DO</a><a>TRAVEL ADVENTURES</a><a>PRODUCTS</a><a>RESOURCES</a><a>REVIEWS</a><a>TEAM</a>
  </nav>
</header>

<section class="abs hero" role="img" aria-label="Silhouette of a climber scaling a rock face at sunset">
  <h1 class="serif">WE SELL<br>T SHIRTS &amp; MORE</h1>
  <p>Sed ut perspiciatis unde omnis iste natus error sit voluptatem accusantium doloremque laudantium, totam rem aperiam, eaque ipsa quae ab illo inventore.</p>
  <span class="pill">SHOP NOW 🛒</span>
  <div class="dots"><i></i><i></i><i class="off"></i><i></i><i></i></div>
</section>

<a class="abs cat shirts" role="img" aria-label="Smiling man wearing a branded T-shirt">T - SHIRTS</a>
<a class="abs cat grooming" role="img" aria-label="Grooming kit with brushes, soap, razor and towel">GROOMING PRODUCTS</a>

<div class="abs sec-head" style="top:1305px"><h2 class="serif" style="position:relative">FEATURED PRODUCTS</h2><a>VIEW ALL</a></div>
<div class="abs row" style="top:1398px">
  <div class="card"><span class="badge" style="left:0;top:14px;transform:rotate(-55deg) translate(-12px,-2px)">FEATURED</span>
    <div class="img" role="img" aria-label="Black T-shirt" style="background:#222"></div>
    <h3>PRODUCT TITLE</h3><div class="sub">Lorem Ipsum Dolor Sit</div><div class="price">$ 532.00</div><div class="old">$ 532.00</div><i class="cart"></i></div>
  <div class="card"><span class="badge" style="right:14px;top:18px">SALE</span>
    <div class="img" role="img" aria-label="Beard oil bottle, brush and soap" style="background:linear-gradient(135deg,#a6461c,#e0d6c4)"></div>
    <h3>PRODUCT TITLE</h3><div class="sub">Lorem Ipsum Dolor Sit</div><div class="price">$ 532.00</div><div class="old">$ 532.00</div><i class="cart"></i></div>
  <div class="card"><div class="tools"><i></i><i></i><i></i></div>
    <div class="img" role="img" aria-label="Grey T-shirt" style="background:#7d7d7f"></div>
    <h3>PRODUCT TITLE</h3><div class="sub">Lorem Ipsum Dolor Sit</div><div class="price">$ 532.00</div><div class="old">$ 532.00</div><i class="cart"></i></div>
  <div class="card faded">
    <div class="img" role="img" aria-label="Skincare bottles" style="background:#f3d9cf;width:170px"></div>
    <span class="stock">OUT OF STOCK</span>
    <h3>PRODUCT TITLE</h3><div class="sub">Lorem Ipsum Dolor Sit</div><div class="price">$ 532.00</div><div class="old">$ 532.00</div><i class="cart"></i></div>
</div>

<section class="abs banner" role="img" aria-label="Climber hanging from a cliff against a cloudy sky">
  <div class="kick">SALE OFF 20% ALL PRODUCTS</div>
  <h2 class="serif">NEW TRENDING<br>COLLECTION</h2>
  <p>Lorem ipsum dolor sit amet, consectetur adipiscing elit.</p>
  <span class="pill">GET STARTED ➔</span>
</section>

<div class="abs sec-head" style="top:2305px"><h2 class="serif" style="position:relative">TRENDING COLLECTIONS</h2><a>VIEW ALL</a></div>
<div class="abs row" style="top:2398px">
  <div class="card"><div class="img" role="img" aria-label="White T-shirt" style="background:#ececec"></div>
    <h3>PRODUCT TITLE</h3><div class="sub">Lorem Ipsum Dolor Sit</div><div class="price">$ 532.00</div><div class="old">$ 532.00</div><i class="cart"></i></div>
  <div class="card"><div class="img" role="img" aria-label="Shaving brush and razor set" style="background:linear-gradient(135deg,#d8d0c2,#3a3a3a);width:170px"></div>
    <h3>PRODUCT TITLE</h3><div class="sub">Lorem Ipsum Dolor Sit</div><div class="price">$ 532.00</div><div class="old">$ 532.00</div><i class="cart"></i></div>
  <div class="card"><div class="img" role="img" aria-label="Blue-grey T-shirt" style="background:#5f7396"></div>
    <h3>PRODUCT TITLE</h3><div class="sub">Lorem Ipsum Dolor Sit</div><div class="price">$ 532.00</div><div class="old">$ 532.00</div><i class="cart"></i></div>
  <div class="card"><div class="img" role="img" aria-label="Black product pouches" style="background:#1b1b1b;width:150px"></div>
    <h3>PRODUCT TITLE</h3><div class="sub">Lorem Ipsum Dolor Sit</div><div class="price">$ 532.00</div><div class="old">$ 532.00</div><i class="cart"></i></div>
</div>

<h2 class="abs serif" style="left:0;width:1200px;top:2822px;text-align:center;font-size:31px">WHAT OUR CUSTOMERS SAY</h2>
<div class="abs quote" style="left:111px">
  <div class="photo" role="img" aria-label="Customer portrait"></div>
  <div class="stars">★★★★★</div><div class="mark">“</div>
  <p>Et harum quidem rerum facilis est et expedita distinctio. Nam libero tempore, cum soluta nobis est eligendi optio cumque.</p>
  <div class="who">- MARA DELKIN</div>
</div>
<div class="abs quote" style="left:612px">
  <div class="photo" role="img" aria-label="Customer portrait"></div>
  <div class="stars">★★★★★</div><div class="mark">“</div>
  <p>Temporibus autem quibusdam et aut officiis debitis aut rerum necessitatibus saepe eveniet ut et voluptates.</p>
  <div class="who">- TOREN ASHBY</div>
</div>

<section class="about">
  <div class="abs about-img" role="img" aria-label="Interior of the barber shop with styling stations"></div>
  <h2 class="serif">ABOUT US</h2>
  <p>Lorem ipsum dolor sit amet, consectetur adipiscing elit, sed do eiusmod tempor incididunt ut labore et dolore magna aliqua. Ut enim ad minim veniam, quis nostrud exercitation ullamco laboris nisi ut aliquip ex ea commodo consequat. Duis aute irure dolor in reprehenderit in voluptate velit esse cillum dolore eu fugiat nulla pariatur. Lorem ipsum dolor sit amet, consectetur adipiscing elit, sed do eiusmod tempor incididunt ut labore et dolore magna aliqua. Ut enim ad minim veniam, quis nostrud exercitation ullamco laboris nisi ut aliquip.</p>
  <span class="pill">READ MORE ➔</span>
</section>

<footer class="abs footer">
  <div class="news">SIGN UP FOR NEWSLETTER</div>
  <div class="email">Enter Your Email</div>
  <div class="subscribe">SUBSCRIBE</div>
  <div class="rule" style="top:155px"></div>
  <div class="flogo"><i class="mark"></i><span>Quellmarrow</span></div>
  <div class="fsocial"><i></i><i></i><i></i><i></i></div>
  <div class="col" style="left:397px;top:218px">
    <h4>CONTACT US</h4>
    <div class="ci"><i class="ic"></i><span>238 , Lorem Ipsum Dolor<br>Fernwick, MI.</span></div>
    <div class="ci" style="align-items:center"><i class="ic"></i><span>info@quellmarrow.com</span></div>
    <div class="ci" style="align-items:center"><i class="ic"></i><span style="font-size:20px;font-weight:500">1 555 204 3178</span></div>
  </div>
  <div class="col" style="left:740px;top:218px"><h4>QUICK LINKS</h4>
    <ul><li>Home</li><li>About Us</li><li>Our Products</li><li>Latest News</li><li>Reviews</li></ul></div>
  <div class="col" style="left:950px;top:218px"><h4>OTHER LINKS</h4>
    <ul><li>Contact Us</li><li>FAQ</li><li>Help Service</li><li>Terms Of Use</li><li>Privacy Policy</li></ul></div>
  <div class="rule" style="top:446px;background:#777"></div>
  <div class="copy">© 2021 Quellmarrow. All Rights Reserved</div>
  <div class="cards"><i></i><i></i><i></i><i></i></div>
</footer>

</body>
</html>
```